Website Re-Design and Refresh

We are looking for a redesign of www.brightlark-example.com the deliverable is a graphic which will be used as a template for the main site.
The Logo will remain the same
The Video currently shown must be included in your submission
Search Element must be included, this should be better visible than it is currently
All navigation current on the left is to be moved to the right.
Top left column should be a “Quick Quotation” element. It should stand out and draw the eye as that is the conversion that we aim for on our site. This is the purpose of the site to attract these.
Add Testimonials navigation that users can click upon.
Below this element on the right “Recent Posts” should become Latest News”
We want users to see how much press coverage the site has had, the following UK’s news logos should be used Morrow Ledger, Evening Quill, NVR and The Wayfarer.
Please use the current text from our site but make some main features which we want to draw attention to. 5 points and use fake text, using a bullet point, icon, graphic or colour to make it stick out the most.
Large Guarantee, shown through a Seal graphic. An example of this type of style is attached.
Updates

Please note that as per the brief we want to havenews/contact forms down the left hand side of the page. This is to comply with “F”shapeeye pattern which shows that users look mostly on the left of webpages.

Please make the quick quotes more distinctive and use of thefields suggested in the brief.

As you appear to like using vivid colours, please see thefollowing examples we like of vivid colours.

 

http://media.tundrasquare.example/cpw-sales/static/images/common/global_nav/nnp_03.png

http://media.tundrasquare.example/cpw-sales/static/sections/homepage/2012_04/images/ban_big_promises.png

http://media.tundrasquare.example/cpw-sales/static/images/landing_pages/mobile_phones/April_2012/mp_hero2_v3.jpg

http://media.tundrasquare.example/cpw-sales/static/sections/upgrades/images/sidebanner_payg_upgrades.gif

Pleaseamend your designs so that they adhere to the following:

 

Thereis a quick quotation form, as per brief, next to the video positionedon the left, the video on the right so they are the first items the userssee. 

 

The"seal" guarantee should be top right and 

Newsand Testimonials should be on the right hand side

 

Inthe main content text area please use latin ipsom lorem text and put 5 bulletpoints in large writing and latin below. Such as:

 

Lorem Ipsum 

Lorem Ipsum 

Lorem Ipsum 

Lorem Ipsum 

Lorem Ipsum 

 

Lorem Ipsum is simply dummy text ofthe printing and typesetting industry. Lorem Ipsum has been the industry'sstandard dummy text ever since the 1500s, when an unknown printer took a galleyof type and scrambled it to make a type specimen book. It has survived not onlyfive centuries, but also the leap into electronic typesetting, remainingessentially unchanged. It was popularised in the 1960s with the release ofLetraset sheets containing Lorem Ipsum passages, and more recently with desktoppublishing software like Orvel SheetCraft including versions of Lorem Ipsum.

The following design is a good indication of style and the use of bright colors. Although the positioning of some elements is not as per the brief. 

Please see best deigns so far:

Target Market(s)

Business To Business

Industry/Entity Type

News

Requirements
Must have
• The Logo will remain the same
Top right should be a “Quick Quotation” element. It should stand out and draw the eye as that is the conversion that we aim for on our site. This is the purpose of the site to attract these.

```html
<!DOCTYPE html>
<html lang="en">
<head>
<meta charset="utf-8">
<title>Brightlark — Only One Reputation</title>
<link rel="stylesheet" href="https://fonts.googleapis.com/css2?family=Arimo:ital,wght@0,400;0,700;1,400;1,700&display=swap">
<style>
:root{
  --green:#7cb342;
  --green-dark:#5f9a2c;
  --ink:#222;
  --body:#666;
  --nav:#a9d6e0;
  --nav-line:#8fc3cf;
  --band:#b8e1e8;
  --panel:#e4e4e4;
  --dark:#2e3035;
  --footer-text:#d8d8d8;
  --white:#fff;
}
*{box-sizing:border-box;margin:0;padding:0}
html,body{width:768px;height:1200px;overflow:hidden;background:var(--white)}
body{font-family:"Arimo",Arial,sans-serif;color:var(--body);position:relative}
.abs{position:absolute}

.brand{left:97px;top:36px;display:flex;align-items:center;gap:8px;font-size:26px;font-weight:700;color:var(--ink)}
.brand-mark{width:22px;height:22px;background:var(--green)}
.callus{right:96px;top:20px;font-size:20px;font-weight:700;color:var(--ink)}
.callus span{color:var(--green)}
.search{left:505px;top:51px;width:132px;height:24px;border:1px solid #bbb;border-radius:3px;font-size:8px;color:#999;padding:7px 8px}
.search-go{left:640px;top:51px;width:32px;height:24px;background:var(--green);border-radius:3px;color:var(--white);font-size:9px;font-weight:700;text-align:center;line-height:24px}

.mainnav{left:96px;top:96px;width:576px;height:29px;background:var(--nav);border-radius:3px;display:flex}
.mainnav a{flex:auto;text-align:center;font-size:9.5px;font-weight:700;color:var(--ink);text-decoration:none;line-height:29px;border-right:1px solid var(--nav-line)}
.mainnav a:last-child{border-right:0}

.quote-head{left:96px;top:144px;width:139px;height:45px;background:var(--green);color:var(--white);font-size:14px;font-weight:700;line-height:15px;padding:8px 9px}
.quote-body{left:96px;top:189px;width:139px;height:134px;background:var(--dark);color:var(--white);font-size:9px;line-height:15px;padding:12px 9px}
.quote-body .phone{font-size:14px;font-weight:700;line-height:22px}
.livechat{left:96px;top:330px;color:var(--green);font-size:15px;font-weight:700}
.livechat-hours{left:96px;top:349px;font-size:9px;line-height:11px;color:var(--body)}
.chat-bubble{left:166px;top:314px}

.news{left:96px;top:377px;width:139px;height:256px;background:var(--panel);border-radius:3px;padding:14px 9px}
.news h3{font-size:9.5px;color:var(--ink);padding-bottom:8px;border-bottom:1px solid var(--green);margin-bottom:12px}
.news p{font-size:8.5px;line-height:11px;color:#888;margin-bottom:9px}

.video{left:241px;top:144px;width:431px;height:213px;background:#000}

.intro{left:241px;top:373px;width:431px}
.intro h1{font-size:26px;color:var(--green);font-weight:700;margin-bottom:17px}
.intro p{font-size:9.3px;line-height:15px;margin-bottom:12px}
.intro b{color:#444}

.press{left:241px;top:608px;width:431px;display:flex;align-items:center;justify-content:space-between;color:#666}
.press .quill{font-size:13px;font-weight:700}
.press .ledger{font-size:9px;letter-spacing:.5px}
.press .badge{width:34px;height:26px;background:#888}
.press .nvr{font-size:16px;font-weight:700;letter-spacing:3px}
.press .wayfarer{font-size:11px}

.band{left:0;top:656px;width:768px;height:344px;background:var(--band)}
.feature{top:684px;width:146px}
.feature h2{font-size:15px;line-height:18px;color:var(--ink);font-weight:700;height:50px;white-space:nowrap}
.feature p{font-size:9.3px;line-height:14px;color:var(--body);width:138px}
.readmore{top:844px;width:74px;height:23px;background:var(--green);border-bottom:2px solid var(--green-dark);border-radius:3px;color:var(--white);font-size:9.5px;font-weight:700;line-height:22px;text-align:center}
.band-rule{left:96px;top:889px;width:579px;height:1px;background:#9fc8cf}
.seal{left:120px;top:904px;width:88px;height:88px}
.guarantee{left:241px;top:912px;font-size:15px;line-height:18px;font-style:italic;color:var(--ink)}
.guarantee b{display:block}
.guarantee-note{left:389px;top:912px;width:140px;font-size:9.3px;line-height:14px}

.footer{left:0;top:1000px;width:768px;height:200px;background:var(--dark)}
.footer-col{top:1022px;width:142px}
.footer-col a{display:block;font-size:8.8px;color:var(--footer-text);text-decoration:none;line-height:16px;border-bottom:1px solid #6a6c70;padding-top:1px}
.footer-col a:last-child{border-bottom:0}
.legal{left:96px;top:1140px;font-size:7px;line-height:9px;color:#9a9a9a}
</style>
</head>
<body>

<div class="abs brand"><span class="brand-mark"></span>Brightlark</div>
<div class="abs callus">Call us on <span>0800 555 0199</span></div>
<div class="abs search">Search</div>
<div class="abs search-go">Go</div>

<nav class="abs mainnav">
  <a href="#">Reputation Management</a>
  <a href="#">Online Reputation Management</a>
  <a href="#">Brand Protection</a>
  <a href="#">Prices</a>
  <a href="#">Testimonials</a>
</nav>

<div class="abs quote-head">Need a<br>Quick Quotation?</div>
<div class="abs quote-body">
  For a simple quotation call our team on:
  <div class="phone">0800 555 0199</div>
  or click <b>here</b> and comlete a brief quotation form and we will respond within 2 working days.
</div>
<div class="abs livechat">Live Chat</div>
<div class="abs livechat-hours">Timings:<br>9.30 am - 5.30 pm</div>
<svg class="abs chat-bubble" width="50" height="42" viewBox="0 0 50 42">
  <path d="M25 2a23 18 0 1 1-12 33l-9 5 4-9A23 18 0 0 1 25 2z" fill="#7cb342" stroke="#fff" stroke-width="1.5"/>
  <text x="25" y="15" text-anchor="middle" font-family="Arimo, Arial, sans-serif" font-size="6.5" fill="#fff">LIVE</text>
  <text x="25" y="23" text-anchor="middle" font-family="Arimo, Arial, sans-serif" font-size="6.5" fill="#fff">CHAT</text>
  <text x="25" y="30" text-anchor="middle" font-family="Arimo, Arial, sans-serif" font-size="5" fill="#fff">SUPPORT</text>
</svg>

<aside class="abs news">
  <h3>Latest News</h3>
  <p>Online Reputation companies are iin demand.</p>
  <p>The Government's new Defamation Bill provides strong protection for authors and...</p>
  <p>Publishers but may limit options for victims of libel.</p>
  <p>Online Reputation companies are iin demand.</p>
  <p>Publishers but may limit options for victims of libel.</p>
  <p>Publishers but may limit options for victims of libel.</p>
</aside>

<div class="abs video" role="img" aria-label="Company introduction video player"></div>

<section class="abs intro">
  <h1>Only One Reputation</h1>
  <p>We understand that <b>you only have one reputation</b> and provide services to both monitor how you are perceived online and reputation management services to allow you to ensure that you are in control of how your business is perceived online.</p>
  <p>Reputation Management is not simply for those who have suffered negative perception previously, but for all businesses to ensure that the most valuable asset they have is protected: <b>their Reputation.</b></p>
  <p><b>Brightlark</b> is a web-based service which provides real-time data to businesses on how their brand, intellectual copyright and overall reputation are portrayed on the internet. By scanning the internet for target words or phrases, the name of business, product brands and the name of key individual a report based on the positive or negative nature of how the business is perceived is returned.</p>
</section>

<div class="abs press">
  <span class="quill">Evening Quill</span>
  <span class="ledger">THE SUNDAY MORROW LEDGER</span>
  <span class="badge" role="img" aria-label="Press badge"></span>
  <span class="nvr">NVR</span>
  <span class="wayfarer">THE WAYFARER</span>
</div>

<div class="abs band"></div>
<div class="abs feature" style="left:96px"><h2>Reputation<br>Management</h2><p>Online reputation management, or ORM, is the practice of consistent research and analysis.</p></div>
<div class="abs feature" style="left:241px"><h2>Online Reputation<br>Management</h2><p>Reputation is the most valuable asset that your business has; it takes years to build. Online reputation management, or ORM, is the practice of consistent research and analysis.</p></div>
<div class="abs feature" style="left:387px"><h2>Online Reputation</h2><p>The Reputation you have on and offline may not be unified.</p></div>
<div class="abs feature" style="left:536px"><h2>Brand Protection</h2><p>Brightlark's Brand Protection service provides you peace of mind.</p></div>
<a class="abs readmore" style="left:96px">› Read more</a>
<a class="abs readmore" style="left:241px">› Read more</a>
<a class="abs readmore" style="left:387px">› Read more</a>
<a class="abs readmore" style="left:533px">› Read more</a>
<div class="abs band-rule"></div>

<svg class="abs seal" viewBox="0 0 88 88" role="img" aria-label="60 day money back guarantee seal">
  <circle cx="44" cy="44" r="42" fill="#c9a24a"/>
  <circle cx="44" cy="44" r="30" fill="#e0bd5e"/>
</svg>
<div class="abs guarantee"><b>Money Back<br>Garantee</b>You don't love it,<br>you don't pay.</div>
<p class="abs guarantee-note">We believe in our products so strongly we offer a Money Back Guarantee.</p>

<footer class="abs footer"></footer>
<div class="abs footer-col" style="left:96px">
  <a href="#">Reputation Management</a>
  <a href="#">Online Reputation Management</a>
  <a href="#">Brand Protection</a>
  <a href="#">Internet Online Defamation</a>
  <a href="#">Online Reputation</a>
  <a href="#">Pro-Active Reputation Management</a>
</div>
<div class="abs footer-col" style="left:241px">
  <a href="#">About Brightlark</a>
  <a href="#">Authors</a>
  <a href="#">Contact</a>
  <a href="#">Reputation Monitoring</a>
  <a href="#">Reputation Correction</a>
</div>
<div class="abs footer-col" style="left:387px;width:140px">
  <a href="#">Prices</a>
  <a href="#">Privacy Policy</a>
  <a href="#">Terms and Conditions of use</a>
</div>
<p class="abs legal">© Copyright Brightlark.<br>All Rights Reserved All Rights Reserved | Vat 000 1234 56 | 4th Floor Linen House | Quarry Street | Harrowby | HB2 7QX</p>

</body>
</html>
```